QorLa Drift Bhutan Trip

This is a one-page (A5) flyer to attract sign ups for Bhutan Trip.

Target Market(s)

Young entrepreneurs (worldwide)

Requirements
Must have
• Must have "WOW" effect and attract sign ups
Nice to have
• Striking and vibrant

```html
<!DOCTYPE html>
<html lang="en">
<head>
<meta charset="utf-8">
<title>QorLa Drift Bhutan Trip</title>
<link rel="stylesheet" href="https://fonts.googleapis.com/css2?family=Montserrat:wght@600;700;800&family=Varela+Round&family=Crimson+Pro:wght@700&display=swap">
<style>
:root{
  --paper:#ffffff;
  --orange:#f24f17;
  --orange-deep:#ee4e14;
  --yellow:#fbe515;
  --gold:#ffd21f;
  --sky:#10bff2;
  --lime:#8cc63f;
  --blue:#2767b0;
  --green:#3aa832;
  --ink:#1f1f1f;
  --grey:#555555;
  --red:#c8102e;
  --footer:#f2f2f2;
  --c-learn:#f04e1c;
  --c-engage:#e8a800;
  --c-discover:#7b2d8e;
  --c-savour:#3aa832;
  --c-immerse:#4a4adf;
  --c-experience:#e0287a;
  --c-rejuvenate:#2aa3dc;
}
*{margin:0;padding:0;box-sizing:border-box}
html,body{width:960px;height:1200px;overflow:hidden;background:var(--paper)}
.flyer{position:relative;width:960px;height:1200px;background:var(--paper);font-family:'Varela Round',sans-serif;color:var(--grey)}
.shapes{position:absolute;inset:0;width:960px;height:1113px}
.brand{position:absolute;left:54px;top:44px;display:flex;align-items:center;gap:14px}
.brand-dot{width:24px;height:24px;border-radius:50%;background:var(--orange)}
.brand-name{font-family:'Montserrat',sans-serif;font-weight:800;font-size:68px;line-height:1;color:var(--ink);letter-spacing:-1px}
.title{position:absolute;left:43px;top:222px;font-family:'Montserrat',sans-serif;font-weight:800;font-size:94px;line-height:1;color:var(--orange);letter-spacing:-1px;white-space:nowrap}
.date{position:absolute;left:220px;top:324px;font-family:'Montserrat',sans-serif;font-weight:700;font-size:46px;line-height:1;color:var(--blue);white-space:nowrap}
.tagline{position:absolute;left:41px;top:562px;font-size:36px;line-height:39px;color:var(--green);white-space:nowrap}
.perks{position:absolute;left:41px;top:698px;list-style:none;font-size:23px;line-height:30px;color:var(--grey);white-space:nowrap}
.perks b{font-family:'Montserrat',sans-serif;font-weight:700;font-size:22px}
.k-learn{color:var(--c-learn)}.k-engage{color:var(--c-engage)}.k-discover{color:var(--c-discover)}
.k-savour{color:var(--c-savour)}.k-immerse{color:var(--c-immerse)}.k-experience{color:var(--c-experience)}.k-rejuvenate{color:var(--c-rejuvenate)}
.register{position:absolute;left:38px;top:957px;font-family:'Crimson Pro',serif;font-weight:700;font-size:34px;line-height:34px;color:var(--red);white-space:nowrap}
.contact{position:absolute;left:38px;top:1030px;display:flex;align-items:center;gap:12px;font-family:'Crimson Pro',serif;font-weight:700;font-size:36px;line-height:1.2;color:var(--ink);white-space:nowrap}
.price{position:absolute;left:589px;top:928px;font-family:'Montserrat',sans-serif;font-weight:800;font-size:54px;line-height:1;color:var(--gold)}
.early{position:absolute;left:592px;top:986px;font-family:'Montserrat',sans-serif;font-weight:700;font-size:25px;color:#fff;white-space:nowrap}
.early-note{position:absolute;left:592px;top:1024px;font-family:'Montserrat',sans-serif;font-weight:600;font-size:16px;color:#fff;white-space:nowrap}
.footer{position:absolute;left:0;top:1113px;width:960px;height:87px;background:var(--footer);font-family:'Crimson Pro',serif;font-weight:700;color:var(--ink)}
.footer-label{position:absolute;font-size:19px;line-height:22px;white-space:nowrap}
.by{left:37px;top:20px}
.support{left:441px;top:30px}
.footer-brand{position:absolute;left:232px;top:14px;font-family:'Montserrat',sans-serif;font-weight:800;font-size:29px;line-height:29px;color:var(--ink)}
.partner{position:absolute;top:33px;display:flex;align-items:center;gap:6px;font-family:'Montserrat',sans-serif;font-weight:700;font-size:13px;line-height:16px;white-space:nowrap}
.partner i{display:block;width:12px;height:12px;border-radius:50%}
.p-lumen{left:566px;color:#3aa832}.p-lumen i{background:#3aa832}
.p-banyan{left:684px;color:#1d4e89}
.p-trail{left:796px;color:#2e8fb8}
</style>
</head>
<body>
<main class="flyer">
  <svg class="shapes" viewBox="161 130 875 1150" preserveAspectRatio="none">
    <defs>
      <linearGradient id="mist" x1="0" y1="0" x2="1" y2="0">
        <stop offset="0" stop-color="#e6e9ef"/><stop offset="0.7" stop-color="#f3f4f7"/><stop offset="1" stop-color="#ffffff"/>
      </linearGradient>
      <linearGradient id="valley" x1="0" y1="0" x2="0" y2="1">
        <stop offset="0" stop-color="#6f9b4a"/><stop offset="0.6" stop-color="#5b7a3e"/><stop offset="1" stop-color="#8a8f8c"/>
      </linearGradient>
      <linearGradient id="temple" x1="0" y1="0" x2="0" y2="1">
        <stop offset="0" stop-color="#c9d7e6"/><stop offset="0.35" stop-color="#a8322a"/><stop offset="0.6" stop-color="#e9e6df"/><stop offset="1" stop-color="#9c9a92"/>
      </linearGradient>
      <linearGradient id="fortress" x1="0" y1="0" x2="0" y2="1">
        <stop offset="0" stop-color="#4f86c2"/><stop offset="0.45" stop-color="#6d8d4f"/><stop offset="1" stop-color="#7c9aa6"/>
      </linearGradient>
    </defs>
    <rect x="161" y="520" width="440" height="190" fill="url(#mist)" role="img" aria-label="Misty snow-capped Himalayan peaks"/>
    <polygon points="665,130 750,130 715,168" fill="var(--orange)"/>
    <polygon points="1036,330 1036,430 985,470 960,430" fill="var(--orange)"/>
    <polygon points="1036,350 1036,650 905,495" fill="var(--yellow)"/>
    <polygon points="1036,700 1036,845 965,772" fill="var(--lime)"/>
    <polygon points="647,264 684,300 647,337 610,300" fill="var(--sky)"/>
    <polygon points="375,1280 740,915 1036,915 1036,1280" fill="var(--yellow)"/>
    <path d="M612,1110 L800,922 L1036,922 L1036,1280 L750,1280 Z" fill="var(--orange-deep)"/>
    <polygon points="740,130 1036,130 1036,300 890,475 650,240" fill="url(#valley)" role="img" aria-label="Hillside temple with a chain bridge and prayer flags"/>
    <polygon points="790,415 1036,645 1036,690 790,940 525,680" fill="url(#temple)" role="img" aria-label="Bhutanese monastery courtyard with a monk walking"/>
    <polygon points="955,810 1036,885 1036,1040 955,1120 800,965" fill="url(#fortress)" role="img" aria-label="Riverside dzong fortress among trees"/>
  </svg>

  <div class="brand"><span class="brand-dot"></span><span class="brand-name">QorLa<br>Drift</span></div>
  <h1 class="title">Bhutan Trip</h1>
  <p class="date">3-6 July 2017</p>

  <p class="tagline">Sign up for a once in<br>a lifetime experience<br>in the land of happiness!</p>

  <ul class="perks">
    <li><b class="k-learn">LEARN</b> from Leading Social Change Makers</li>
    <li><b class="k-engage">ENGAGE</b> the community through volunteering</li>
    <li><b class="k-discover">DISCOVER</b> your inner happiness</li>
    <li><b class="k-savour">SAVOUR</b> Organic food</li>
    <li><b class="k-immerse">IMMERSE</b> in traditional sports and craft</li>
    <li><b class="k-experience">EXPERIENCE</b> warm Bhutanese hospitality</li>
    <li><b class="k-rejuvenate">REJUVENATE</b> your mind, body and soul</li>
  </ul>

  <p class="register">Register now!<br>Limited to 30 participants!</p>
  <p class="contact">
    <svg width="30" height="22" viewBox="0 0 30 22" aria-hidden="true"><rect x="1" y="1" width="28" height="20" fill="none" stroke="#1f1f1f" stroke-width="2"/><path d="M1 1 L15 12 L29 1 M1 21 L11 10 M29 21 L19 10" fill="none" stroke="#1f1f1f" stroke-width="2"/></svg>
    hello@lumentrust.org
  </p>

  <p class="price">$2800/-</p>
  <p class="early">Early bird discount $2300/-</p>
  <p class="early-note">(If you sign up by 31 March 2017)</p>

  <footer class="footer">
    <p class="footer-label by">Exclusively Brought<br>To You By:</p>
    <p class="footer-brand">QorLa<br>Drift</p>
    <p class="footer-label support">Supported By:</p>
    <p class="partner p-lumen"><i></i>Lumen Trust</p>
    <p class="partner p-banyan">Banyan Circle</p>
    <p class="partner p-trail">Trailnest</p>
  </footer>
</main>
</body>
</html>
```